Business card design for IT consulting company

Looking for a simple, modern, clean business card design.
Open to reworking our existing logo.

Attached is our current business cards which we do not like.
Ideally double sided with something simple on the back.
Rectangle / Horizonal only.
No rounded edges on the card.
White as the dominate color is preferred.

Target Market(s)

clients, legal, oil & gas, medical, professionals

Industry/Entity Type

IT, tech, consulting

Contact Information for Business Card

Name, Title, email, phone, cell, website

Font styles to use
Sans Serif

Requirements
Must have
• Clean design
Should not have
• loud colors or unusual fonts, etc

```html
<!DOCTYPE html>
<html lang="en">
<head>
<meta charset="utf-8">
<title>Norvane Solutions – Business Card</title>
<link href="https://fonts.googleapis.com/css2?family=Montserrat:wght@400;600;700&family=Mulish:wght@400;600&display=swap" rel="stylesheet">
<style>
  :root {
    --bg: #3b3b3d;
    --card-dark: #161616;
    --card-light: #ffffff;
    --red: #ef4058;
    --navy: #2a2a73;
    --blue: #45b0e3;
    --ink: #1c1c1c;
  }
  * { margin: 0; padding: 0; box-sizing: border-box; }
  html, body { width: 1200px; height: 689px; overflow: hidden; }
  body {
    background: var(--bg);
    font-family: "Mulish", sans-serif;
    position: relative;
  }
  .card {
    position: absolute;
    top: 190px;
    width: 540px;
    height: 309px;
    overflow: hidden;
  }
  .card--back { left: 40px; background: var(--card-dark); }
  .card--front { left: 620px; background: var(--card-light); }

  .back-brand {
    position: absolute;
    inset: 0;
    display: flex;
    align-items: center;
    justify-content: center;
    gap: 18px;
  }
  .brand-square {
    width: 58px; height: 58px;
    background: var(--red);
  }
  .brand-name {
    font-family: "Montserrat", sans-serif;
    font-weight: 700;
    font-size: 44px;
    color: #ffffff;
    letter-spacing: 0.5px;
  }

  .front-brand {
    position: absolute;
    top: 34px; right: 36px;
    display: flex;
    align-items: center;
    gap: 10px;
  }
  .front-brand .brand-square { width: 34px; height: 34px; background: var(--navy); }
  .front-brand .brand-name { font-size: 26px; color: var(--navy); }

  .person {
    position: absolute;
    left: 40px; top: 108px;
  }
  .person-name {
    font-family: "Montserrat", sans-serif;
    font-weight: 400;
    font-size: 26px;
    letter-spacing: 0.5px;
    color: var(--red);
  }
  .person-name .surname { color: var(--blue); }
  .person-title { font-size: 13px; color: var(--ink); margin-top: 2px; }

  .contact {
    position: absolute;
    left: 40px; top: 186px;
    list-style: none;
    font-size: 14px;
    line-height: 21px;
    color: var(--ink);
  }
  .contact li { display: flex; align-items: center; gap: 8px; }
  .contact svg { width: 13px; height: 13px; flex: none; }

  .wave { position: absolute; left: 0; bottom: 0; width: 540px; height: 309px; }
</style>
</head>
<body>
  <section class="card card--back">
    <div class="back-brand">
      <div class="brand-square"></div>
      <span class="brand-name">Norvane Solutions</span>
    </div>
  </section>

  <section class="card card--front">
    <div class="front-brand">
      <div class="brand-square"></div>
      <span class="brand-name">Norvane</span>
    </div>

    <div class="person">
      <h1 class="person-name">DANIEL <span class="surname">REYES</span></h1>
      <p class="person-title">IT Consultant</p>
    </div>

    <ul class="contact">
      <li>
        <svg viewBox="0 0 16 16"><rect x="1" y="3" width="14" height="10" fill="var(--red)"/><path d="M1 3 L8 9 L15 3" fill="none" stroke="#fff" stroke-width="1.5"/></svg>
        daniel.reyes@norvane.ca
      </li>
      <li>
        <svg viewBox="0 0 16 16"><path d="M3 1 L6 1 L7 5 L5 6.5 C6 9 7 10 9.5 11 L11 9 L15 10 L15 13 C15 14 14 15 13 15 C6 15 1 10 1 3 C1 2 2 1 3 1Z" fill="var(--red)"/></svg>
        (800) 555-0148
      </li>
      <li>
        <svg viewBox="0 0 16 16"><rect x="4" y="1" width="8" height="14" rx="1.5" fill="none" stroke="var(--red)" stroke-width="1.5"/><circle cx="8" cy="12.5" r="0.9" fill="var(--red)"/></svg>
        (604) 555-0193
      </li>
      <li>
        <svg viewBox="0 0 16 16" fill="none" stroke="var(--red)" stroke-width="1.2"><circle cx="8" cy="8" r="6.5"/><ellipse cx="8" cy="8" rx="3" ry="6.5"/><path d="M1.5 8 H14.5 M2.5 4.8 H13.5 M2.5 11.2 H13.5"/></svg>
        www.norvane.ca
      </li>
    </ul>

    <svg class="wave" viewBox="0 0 540 309" preserveAspectRatio="none" aria-hidden="true">
      <path d="M120 309 C 250 262 340 200 410 140 C 460 100 500 82 540 80 L540 309 Z" fill="var(--red)"/>
      <path d="M95 309 C 230 262 330 190 400 132 C 455 88 495 72 540 70" fill="none" stroke="var(--navy)" stroke-width="4"/>
    </svg>
  </section>
</body>
</html>
```